Wolkenfeld - a property developer - Website design

Hi all!
Exciting new project for you! :)
We are looking for some creative/modern designs to best represent us as a company.
Please have a look at the following link: huhu.wolkenfeld.eu to get an idea about who we are and what we do.
The 'Main Page' of the HP should be neatly arranged, easy to navigate, contain several pictures (changing every 10 seconds or so) that should reflect that we are property developers.
The navigation points ('About us', 'Projects' 'Investment', 'Contact Us', 'Legal Notice') should be included in the Design (again under every navigation point, pictures may be added - that reflect our profession and/or the subsection)
What we will need at the end of the day is a fully functional site - i.e: a site that is designed and programmed with backend/wordpress, to allow us to make changes anytime we feel like it.
Further questions?! Don't hesitate to contact me! Thanks :)
Target Market(s)
Real Estate Development/Building sector
Industry/Entity Type
Real Estate Development
Number of Pages Required
5+ page
Look and feel

```html
<!DOCTYPE html>
<html lang="en">
<head>
<meta charset="utf-8">
<title>Wolkenfeld – Luxury Villa</title>
<link rel="stylesheet" href="https://fonts.googleapis.com/css2?family=Open+Sans:ital,wght@0,400;0,600;0,700;1,400&family=Raleway:wght@700;800&family=Playfair+Display:ital@1&display=swap">
<style>
:root{
  --teal:#6db3be;
  --teal-deep:#4f9ba8;
  --navy:#232a3b;
  --ink:#222326;
  --text:#7d7d7d;
  --grey-band:#e5e5e5;
  --page:#f2f2f2;
  --white:#ffffff;
}
*{margin:0;padding:0;box-sizing:border-box}
html,body{width:1200px;height:3000px;overflow:hidden}
body{position:relative;background:var(--page);font-family:'Open Sans',Arial,sans-serif;color:var(--ink)}
.abs{position:absolute}
.photo{position:absolute}

/* hero */
.hero{position:absolute;left:0;top:0;width:1200px;height:938px;overflow:hidden}
.hero-photo{left:0;top:0;width:1200px;height:938px;background:linear-gradient(100deg,#f4f6f6 0%,#e7ecec 40%,#a9d4d8 62%,#bfe0e2 75%,#d9dcdc 100%)}
.hero-bed{left:400px;top:380px;width:800px;height:558px;background:linear-gradient(180deg,rgba(226,229,230,0) 0%,rgba(226,229,230,.9) 22%,#d5d8da 50%,#2a2a2c 68%,#1f1f21 100%)}
.nav{left:432px;top:0;width:768px;height:68px;background:rgba(28,30,34,.82);display:flex;align-items:center;padding-left:30px}
.nav a{color:var(--white);font-weight:700;font-size:15px;text-decoration:none;margin-right:32px;letter-spacing:.2px}
.nav a.active{color:var(--teal)}
.nav .burger{position:absolute;right:24px;top:27px;width:22px}
.nav .burger i{display:block;height:2px;background:var(--white);margin-bottom:5px}
.info-panel{left:50px;top:0;width:280px;height:938px;background:var(--teal);color:var(--white);border-left:6px solid #8cc6ce}
.info-panel .rule{position:absolute;left:22px;width:224px;height:1px;background:rgba(255,255,255,.45)}
.info-panel p{position:absolute;left:22px;font-size:15px;line-height:28px}
.price-label{position:absolute;left:22px;top:490px;font-size:23px;font-weight:700}
.price{position:absolute;left:22px;top:530px;font-size:35px;font-weight:700}
.visit-btn{position:absolute;left:40px;top:610px;width:184px;height:46px;background:var(--ink);color:var(--white);font-weight:700;font-size:15px;display:flex;align-items:center;justify-content:center;letter-spacing:.4px}

/* about */
.about{left:0;top:938px;width:1200px;height:652px;background:var(--white)}
.about-photo{left:56px;top:90px;width:280px;height:468px;background:linear-gradient(180deg,#d9ecf6 0%,#eef2f2 40%,#8a7a68 60%,#5d8b3c 85%,#86b24a 100%)}
.corner{position:absolute;width:30px;height:30px;border-color:var(--white);border-style:solid}
.kicker{font-family:'Playfair Display',Georgia,serif;font-style:italic;font-size:13px;color:var(--text)}
.heading{font-family:'Raleway',Arial,sans-serif;font-weight:800;font-size:20px;letter-spacing:.6px}
.bar{height:2px;width:80px;background:var(--teal)}
.body-text{font-size:14px;line-height:24px;color:var(--text)}
.feature{position:absolute;top:416px;width:160px;text-align:center}
.feature svg{display:block;margin:0 auto}
.feature .label{font-size:13px;font-weight:700;margin-top:12px;letter-spacing:.3px}
.feature .count{font-family:'Playfair Display',Georgia,serif;font-style:italic;font-size:28px;margin-top:4px}

/* highlights */
.highlights{left:0;top:1590px;width:1200px;height:474px}
.room-photo{left:0;top:0;width:492px;height:474px;background:linear-gradient(180deg,#f5f5f3 0%,#e9e8e4 45%,#c9455a 62%,#eeeeee 70%,#4b4440 100%)}
.panel-dark{left:492px;top:0;width:708px;height:474px;background:var(--navy);color:var(--white)}
.hl{position:absolute;width:270px}
.hl h4{color:var(--teal);font-size:13px;font-weight:700;letter-spacing:.3px;margin-bottom:10px}
.hl p{color:#9aa0ab;font-size:13px;line-height:23px}

/* intro band */
.intro{left:0;top:2064px;width:1200px;height:222px;background:var(--grey-band)}
.intro .body-text{font-style:italic;font-size:13.5px;line-height:25px;color:#6f6f6f}

/* gallery */
.gallery{left:0;top:2286px;width:1200px;height:714px;background:var(--page)}
.filter{left:52px;top:188px;width:1096px;height:48px;border-top:1px solid #cfcfcf;border-bottom:1px solid #cfcfcf;display:flex;align-items:center;justify-content:center;font-size:13px;color:#666}
.filter span{margin:0 21px;position:relative}
.filter .sep{margin:0;color:#888}
.filter .active{color:var(--teal-deep)}
.filter .active::after{content:"";position:absolute;left:-6px;right:-6px;top:31px;height:1px;background:var(--teal-deep)}
</style>
</head>
<body>

<section class="hero">
  <div class="photo hero-photo" role="img" aria-label="Bright bedroom with turquoise floral wallpaper and a dark wooden bed"></div>
  <div class="photo hero-bed" role="img" aria-label="Bed with white linen and turquoise cushions"></div>
  <nav class="abs nav">
    <a class="active">HOME</a><a>ABOUT US</a><a>PROJECTS</a><a>INVESTMENT</a><a>CONTACT US</a><a>'LEGAL NOTICE'</a>
    <span class="burger"><i></i><i></i><i></i></span>
  </nav>
  <aside class="abs info-panel">
    <div class="rule" style="top:108px"></div>
    <p style="top:142px">48, Birchmoor Lane, Lindenport,<br>LP- 20417, Northland</p>
    <div class="rule" style="top:245px"></div>
    <p style="top:290px">2 BATHROOM</p>
    <p style="top:332px">2 DRAWINGROOM</p>
    <p style="top:374px">3150 SQ.FT</p>
    <div class="rule" style="top:450px"></div>
    <div class="price-label">Price:</div>
    <div class="price">$ 2,689,500</div>
    <div class="visit-btn">SHEDULE VISIT</div>
  </aside>
</section>

<section class="abs about">
  <div class="photo about-photo" role="img" aria-label="Modern white villa with wooden balconies and a garden">
    <span class="corner" style="left:8px;top:8px;border-width:2px 0 0 2px"></span>
    <span class="corner" style="right:8px;top:8px;border-width:2px 2px 0 0"></span>
    <span class="corner" style="left:8px;bottom:8px;border-width:0 0 2px 2px"></span>
    <span class="corner" style="right:8px;bottom:8px;border-width:0 2px 2px 0"></span>
  </div>
  <div class="abs kicker" style="left:430px;top:94px">A Few Words About House</div>
  <h2 class="abs heading" style="left:430px;top:120px">ELMSTEAD LUXUARY VILLA</h2>
  <div class="abs bar" style="left:430px;top:156px;width:58px;background:var(--ink)"></div>
  <p class="abs body-text" style="left:430px;top:182px;width:730px">Neque porro quisquam est, qui dolorem ipsum quia dolor sit amet, consectetur, adipisci velit, sed quia non numquam eius modi tempora incidunt ut labore et dolore magnam aliquam quaerat voluptatem. Ut enim ad minima veniam, quis nostrum exercitationem ullam corporis suscipit laboriosam.</p>
  <p class="abs body-text" style="left:430px;top:266px;width:730px">Neque porro quisquam est, qui dolorem ipsum quia dolor sit amet, consectetur, adipisci velit, sed quia non numquam eius modi tempora incidunt ut labore et dolore magnam aliquam.</p>
  <div class="abs" style="left:430px;top:366px;width:730px;height:1px;background:#e3e3e3"></div>

  <div class="feature" style="left:440px">
    <svg width="44" height="46" viewBox="0 0 44 46" fill="var(--teal)"><path d="M8 22a14 14 0 0 1 28 0z"/><rect x="20" y="2" width="4" height="8"/><rect x="6" y="22" width="32" height="4"/><g><circle cx="12" cy="32" r="2"/><circle cx="22" cy="32" r="2"/><circle cx="32" cy="32" r="2"/><circle cx="17" cy="39" r="2"/><circle cx="27" cy="39" r="2"/><circle cx="22" cy="45" r="1.6"/></g></svg>
    <div class="label">BATHROOM</div><div class="count">2</div>
  </div>
  <div class="feature" style="left:620px">
    <svg width="50" height="46" viewBox="0 0 50 46" fill="var(--teal)"><rect x="4" y="6" width="42" height="22" rx="3"/><rect x="10" y="12" width="12" height="8" rx="2" fill="#fff"/><rect x="28" y="12" width="12" height="8" rx="2" fill="#fff"/><rect x="2" y="28" width="46" height="8"/><rect x="4" y="36" width="4" height="6"/><rect x="42" y="36" width="4" height="6"/></svg>
    <div class="label">BEDROOM</div><div class="count">3</div>
  </div>
  <div class="feature" style="left:800px">
    <svg width="50" height="46" viewBox="0 0 50 46" fill="var(--teal)"><path d="M6 12h38a4 4 0 0 1 4 4v18H2V16a4 4 0 0 1 4-4z"/><rect x="9" y="18" width="32" height="8" rx="3" fill="#fff"/><rect x="4" y="34" width="4" height="6"/><rect x="42" y="34" width="4" height="6"/></svg>
    <div class="label">KIDSROOM</div><div class="count">1</div>
  </div>
  <div class="feature" style="left:980px">
    <svg width="50" height="46" viewBox="0 0 50 46" fill="var(--teal)"><rect x="6" y="6" width="38" height="14" rx="3"/><rect x="12" y="10" width="26" height="6" rx="2" fill="#fff"/><rect x="2" y="22" width="46" height="14" rx="2"/><rect x="2" y="28" width="46" height="2" fill="#fff"/><rect x="4" y="36" width="4" height="5"/><rect x="42" y="36" width="4" height="5"/></svg>
    <div class="label">GUESTROOM</div><div class="count">2</div>
  </div>
</section>

<section class="abs highlights">
  <div class="photo room-photo" role="img" aria-label="Bright bedroom with red bedding, ceiling fan and garden window"></div>
  <div class="abs panel-dark">
    <h3 class="abs heading" style="left:86px;top:70px;color:var(--white)">PROPERTY HIGHLIGHTS</h3>
    <div class="abs bar" style="left:86px;top:108px"></div>
    <div class="hl" style="left:86px;top:148px"><h4>FABULOUS VIEW</h4><p>Neque porro quisquam est, qui dolorem ipsum quia dolor sit amet, consectetur adipisci velit, sed quia non numquam</p></div>
    <div class="hl" style="left:386px;top:148px"><h4>LARGE PLAY GROUND</h4><p>Neque porro quisquam est, qui dolorem ipsum quia dolor sit amet, consectetur adipisci velit, sed quia non numquam</p></div>
    <div class="hl" style="left:86px;top:290px"><h4>QUIET NEIGHBOURHOOD</h4><p>Neque porro quisquam est, qui dolorem ipsum quia dolor sit amet, consectetur adipisci velit, sed quia non numquam</p></div>
    <div class="hl" style="left:386px;top:290px"><h4>SWIMMING POOL</h4><p>Neque porro quisquam est, qui dolorem ipsum quia dolor sit amet, consectetur adipisci velit, sed quia non numquam</p></div>
  </div>
</section>

<section class="abs intro">
  <div class="abs kicker" style="left:52px;top:72px">A Few Words About House</div>
  <h2 class="abs heading" style="left:52px;top:104px">LUXURY VILLA</h2>
  <div class="abs bar" style="left:52px;top:142px;background:#555"></div>
  <p class="abs body-text" style="left:334px;top:74px;width:816px">Neque porro quisquam est, qui dolorem ipsum quia dolor sit amet, consectetur, adipisci velit, sed quia non numquam eius modi tempora incidunt ut labore et dolore magnam aliquam quaerat voluptatem. Ut enim ad minima veniam, quis nostrum exercitationem ullam corporis suscipit laboriosam.</p>
</section>

<section class="abs gallery">
  <div class="abs kicker" style="left:0;width:1200px;text-align:center;top:76px">Tour Of Our Villa</div>
  <h2 class="abs heading" style="left:0;width:1200px;text-align:center;top:102px;font-size:22px">CHECKOUT VILLA PHOTOS</h2>
  <div class="abs bar" style="left:560px;top:140px"></div>
  <div class="abs filter">
    <span>ALL IMAGES</span><span class="sep">/</span><span class="active">INTEROORS</span><span class="sep">/</span><span>KITCHEN</span><span class="sep">/</span><span>BEDROOM</span><span class="sep">/</span><span>DRAWING ROOM</span><span class="sep">/</span><span>BALCONY</span><span class="sep">/</span><span>BATHROOM</span><span class="sep">/</span><span>TOP ROOF</span>
  </div>
  <div class="photo" style="left:52px;top:266px;width:722px;height:370px;background:linear-gradient(90deg,#3f78a8 0%,#e9eef0 20%,#f4f4f2 55%,#2f6aa3 75%,#3a74ab 100%)" role="img" aria-label="Modern kitchen with blue walls, island and bar stools"></div>
  <div class="photo" style="left:802px;top:266px;width:346px;height:170px;background:linear-gradient(180deg,#eceae6 0%,#dcd9d3 55%,#6e6a66 100%)" role="img" aria-label="Living room with grey sofa and cushions"></div>
  <div class="photo" style="left:802px;top:466px;width:346px;height:170px;background:linear-gradient(180deg,#7fa9c8 0%,#a7b49a 45%,#b59a7c 80%,#8b7358 100%)" role="img" aria-label="Stone balcony with chairs overlooking a lake"></div>
</section>

</body>
</html>
```